"Fight Back" banner ad design

We have sketched the design and have images to consider including. We are looking for something striking, FIGHT BACK! with a clenched fist image, then a fading images of variance.png and hi-bill.png in the background. Tag line "Fight your water bill with your own data" optionally include "Crest View" rivo3159 logo, KMPT Design, LLC based in San Diego CA. Pre-order now, visit https://www.raisenest.com/rivoplume @rivo3159, info@rivo3159.com

"Fight your water bill with your own data"

```html
<!DOCTYPE html>
<html lang="en">
<head>
<meta charset="utf-8">
<title>Fight Your Water Bill – rivo3159</title>
<link rel="stylesheet" href="https://fonts.googleapis.com/css2?family=Arimo:ital,wght@0,400;0,700;1,700&display=swap">
<style>
  :root {
    --sky-light: #ffffff;
    --sky-blue: #a9cce6;
    --band-blue: #3f8fd2;
    --teal-dark: #2f6f80;
    --teal: #4a8fa1;
    --teal-text: #3c8b9c;
    --cyan-soft: #c6f1f3;
    --slate-dark: #4a4a4a;
    --slate: #6a6a6a;
    --yellow-soft: #f2f29a;
    --table-head: #1f5f6e;
    --table-total: #8fd2de;
    --ink: #111111;
    --white: #ffffff;
  }
  * { box-sizing: border-box; margin: 0; padding: 0; }
  html, body { width: 900px; height: 1200px; overflow: hidden; background: var(--white); }
  body { font-family: "Arimo", Arial, sans-serif; }

  .ad { position: relative; width: 900px; height: 1200px; overflow: hidden; border: 1px solid #555; }
  .ad-backdrop { position: absolute; inset: 0; }

  .fist-photo {
    position: absolute; left: 340px; top: 24px; width: 222px; height: 300px;
    border-radius: 90px 90px 10px 10px;
    background: linear-gradient(180deg, #c98e6a 0%, #b87550 60%, #a0623f 100%);
  }

  .tagline {
    position: absolute; left: 84px; top: 366px;
    color: var(--white); font-weight: 700; font-style: italic;
    font-size: 53px; line-height: 57px;
    text-shadow: 1px 2px 3px rgba(0,0,0,.35);
  }
  .studio {
    position: absolute; left: 20px; width: 410px; top: 607px;
    text-align: center; color: var(--cyan-soft); font-weight: 700;
    font-size: 34px; line-height: 41px;
  }

  .brand-name {
    position: absolute; left: 592px; top: 728px;
    color: var(--teal-text); font-weight: 700; font-size: 27px;
  }

  .campaign-box {
    position: absolute; left: 10px; top: 788px; width: 430px; height: 405px;
    background: linear-gradient(180deg, var(--slate) 0%, var(--slate-dark) 100%);
    border: 1px solid #333;
  }
  .campaign-box__bar {
    height: 22px;
    background: linear-gradient(180deg, #f2f2f2 0%, #9a9a9a 100%);
  }
  .campaign-box__title {
    margin-top: 26px; text-align: center; color: var(--white);
    font-weight: 700; font-size: 74px; line-height: 80px; letter-spacing: 1px;
    text-shadow: 0 2px 0 #9b9b9b, 0 4px 6px rgba(0,0,0,.6);
  }
  .campaign-box__rule { margin-top: 22px; height: 2px; background: #8a8a8a; }
  .campaign-box__cta {
    margin-top: 24px; text-align: center; color: var(--yellow-soft);
    font-weight: 700; font-size: 33px; line-height: 37px;
  }
  .campaign-box__link {
    margin-top: 18px; text-align: center; color: var(--white); font-size: 15px;
  }
  .campaign-box__email {
    margin-top: 16px; text-align: center; color: var(--white);
    font-weight: 700; font-size: 19px;
  }

  .bill {
    position: absolute; left: 459px; top: 783px; width: 434px; height: 412px;
    background: var(--white); border: 2px solid var(--ink);
    font-size: 15px; color: var(--ink); line-height: 19px;
  }
  .bill__head {
    background: var(--table-head); color: var(--white); text-align: center;
    font-weight: 700; font-size: 18px; line-height: 22px;
  }
  .bill__body { padding: 10px 26px 0 5px; }
  .bill__section { font-weight: 700; }
  .bill__row { display: flex; justify-content: space-between; padding-left: 14px; }
  .bill__usage { display: flex; padding-left: 14px; }
  .bill__usage span:nth-child(1) { width: 96px; }
  .bill__usage span:nth-child(2) { width: 34px; }
  .bill__tier {
    display: grid; grid-template-columns: 29px 40px 52px 8px 36px 18px 76px 1fr;
  }
  .bill__tier .num, .bill__tier .amt { text-align: right; }
  .bill__tier .label { grid-column: 2; }
  .bill__tier-rate {
    display: grid; grid-template-columns: 259px 1fr;
  }
  .bill__tier-rate .rate { text-align: right; }
  .bill__tier-rate .rule { border-bottom: 1px solid var(--ink); margin: 0 0 4px 18px; }
  .bill__gap { height: 20px; }
  .bill__gap--lg { height: 36px; }
  .bill__total-row { display: flex; justify-content: space-between; font-weight: 700; }
  .bill__plain-row { display: flex; justify-content: space-between; }
  .bill__due {
    position: absolute; left: 0; right: 0; bottom: 0; height: 24px;
    background: var(--table-total); border-top: 2px solid var(--ink);
    display: flex; justify-content: space-between; padding: 0 26px 0 5px;
    font-weight: 700; font-size: 19px; line-height: 22px;
  }
</style>
</head>
<body>
<main class="ad">
  <svg class="ad-backdrop" width="900" height="1200" viewBox="0 0 900 1200" aria-hidden="true">
    <defs>
      <radialGradient id="sky" cx="0.5" cy="0.05" r="0.75">
        <stop offset="0" stop-color="#ffffff"/>
        <stop offset="0.55" stop-color="#dcecf7"/>
        <stop offset="1" stop-color="#a9cce6"/>
      </radialGradient>
      <linearGradient id="panel" x1="0" y1="0" x2="0" y2="1">
        <stop offset="0" stop-color="#2f6f80"/>
        <stop offset="1" stop-color="#4b93a5"/>
      </linearGradient>
      <linearGradient id="drops" x1="0" y1="0" x2="0" y2="1">
        <stop offset="0" stop-color="#a9c7d8"/>
        <stop offset="0.55" stop-color="#cfe1ea"/>
        <stop offset="1" stop-color="#ffffff"/>
      </linearGradient>
      <linearGradient id="band" x1="0" y1="0" x2="0" y2="1">
        <stop offset="0" stop-color="#8cc2ee"/>
        <stop offset="1" stop-color="#3a84c8"/>
      </linearGradient>
    </defs>
    <rect width="900" height="380" fill="url(#sky)"/>
    <polygon points="0,250 451,380 451,784 0,784" fill="url(#panel)"/>
    <g role="img" aria-label="Water droplets on glass">
      <polygon points="451,380 900,256 900,720 451,720" fill="url(#drops)"/>
    </g>
    <polygon points="0,236 451,358 900,238 900,262 451,386 0,262" fill="url(#band)"/>
    <polyline points="0,258 451,380 900,258" fill="none" stroke="#ffffff" stroke-width="3"/>
  </svg>

  <div class="fist-photo" role="img" aria-label="Raised clenched fist"></div>

  <h1 class="tagline">Fight Your<br>Water Bill<br>With your<br>Own Data</h1>
  <p class="studio">KMPT Design,<br>LLC based<br>in San Diego,<br>CA</p>

  <p class="brand-name">rivo3159</p>

  <section class="campaign-box">
    <div class="campaign-box__bar"></div>
    <h2 class="campaign-box__title">CREST<br>VIEW</h2>
    <div class="campaign-box__rule"></div>
    <p class="campaign-box__cta">Pre-Order Now,<br>visit:</p>
    <p class="campaign-box__link">Https://www.Raisenest.com/rivoplume @rivo3159</p>
    <p class="campaign-box__email">Info@rivo3159.com</p>
  </section>

  <section class="bill">
    <div class="bill__head">FEES &amp; CHARGES</div>
    <div class="bill__body">
      <div class="bill__section">Water Services</div>
      <div class="bill__row"><span>Single Family Residential Base Fee</span><span>48.44</span></div>
      <div class="bill__usage"><span>Water Used</span><span>65</span><span>HCF</span></div>
      <div class="bill__tier"><span class="label">Tier 1</span><span class="num">8.00</span><span></span><span>HCF</span><span>@</span><span class="num">$4.8425</span><span class="amt">38.74</span></div>
      <div class="bill__tier"><span class="label">Tier 2</span><span class="num">16.00</span><span></span><span>HCF</span><span>@</span><span class="num">$5.4231</span><span class="amt">86.77</span></div>
      <div class="bill__tier"><span class="label">Tier 3</span><span class="num">12.00</span><span></span><span>HCF</span><span>@</span><span class="num">$7.7483</span><span class="amt">92.98</span></div>
      <div class="bill__tier"><span class="label">Tier 4</span><span class="num">29.00</span><span></span><span>HCF</span><span>@</span><span></span><span class="amt">315.96</span></div>
      <div class="bill__tier-rate"><span class="rate">$10.8952</span><span class="rule"></span></div>
      <div class="bill__row"><span>Total Charge for Water Used</span><span>534.45</span></div>
      <div class="bill__gap"></div>
      <div class="bill__section">Sewer &amp; Storm Drain Services</div>
      <div class="bill__row"><span>Sewer Base Fee</span><span>30.66</span></div>
      <div class="bill__row"><span>Sewer Service Charge</span><span>60.17</span></div>
      <div class="bill__row"><span>Storm Drain</span><span>1.90</span></div>
      <div class="bill__gap--lg"></div>
      <div class="bill__total-row"><span>Total Current Charges</span><span>675.62</span></div>
      <div class="bill__plain-row"><span>Deferred Due</span><span>79.66</span></div>
    </div>
    <div class="bill__due"><span>TOTAL DUE</span><span>755.28</span></div>
  </section>
</main>
</body>
</html>
```